bail bonds business

Need a web design for a Bail Bond company. At Larkmoor Bails, we specialize in getting arrested defendants out of jail. Also, I have all the necessary information already uploaded in the files.

Target Market(s)

Arrested defendants and their families who will post bails on their behalf.

Industry/Entity Type

Business

Coding

Coded - Design and coding required

Number of Pages Required

1 page

```html
<!DOCTYPE html>
<html lang="en">
<head>
<meta charset="utf-8">
<title>Larkmoor Bails Inc.</title>
<link href="https://fonts.googleapis.com/css2?family=Raleway:wght@300;400;600;700;800&family=Open+Sans:wght@400;600;700&display=swap" rel="stylesheet">
<style>
:root{
  --red:#c4161c;
  --dark:#111111;
  --charcoal:#2b2b2b;
  --grey:#6b6b6b;
  --light:#f1f1f1;
  --white:#ffffff;
}
*{box-sizing:border-box;margin:0;padding:0}
html,body{width:727px;height:1200px;overflow:hidden}
body{font-family:'Open Sans',sans-serif;color:var(--charcoal);background:var(--white);position:relative}
.header{height:80px;position:relative;background:var(--white);box-shadow:0 1px 3px rgba(0,0,0,.08);z-index:2}
.brand{position:absolute;left:28px;top:12px;display:flex;align-items:center;gap:8px}
.brand-mark{width:26px;height:26px;background:var(--red)}
.brand-name{font-family:'Raleway',sans-serif;font-weight:800;font-size:14px;color:var(--charcoal);letter-spacing:.5px}
.topline{position:absolute;right:28px;top:8px;display:flex;align-items:center;gap:6px;font-size:9px;color:var(--red);font-weight:600}
.topline .dot{width:12px;height:12px;border-radius:50%;background:#cfcfcf}
.nav{position:absolute;right:20px;top:40px;display:flex;font-family:'Raleway',sans-serif;font-size:9px;font-weight:700;letter-spacing:.4px}
.nav a{color:var(--charcoal);text-decoration:none;padding:8px 14px;border-left:1px solid #e2e2e2}
.nav a.active{color:var(--red);border-bottom:2px solid var(--red)}
.hero{position:absolute;top:80px;left:0;width:727px;height:338px;background:linear-gradient(180deg,#fafafa,#ececec)}
.hero-photo{position:absolute;right:0;top:0;width:400px;height:320px;background:radial-gradient(circle at 55% 35%,#9a9a9a 0,#5c5c5c 22%,#d8d8d8 46%,#efefef 70%)}
.hero-copy{position:absolute;left:30px;top:60px}
.hero-title{font-family:'Raleway',sans-serif;font-weight:400;font-size:64px;color:var(--red);letter-spacing:2px;line-height:1}
.hero-sub{font-family:'Raleway',sans-serif;font-weight:400;font-size:25px;color:#444;margin-top:8px;letter-spacing:.5px}
.hero-list{list-style:none;margin-top:14px;font-family:'Raleway',sans-serif;font-weight:700;font-size:12px;color:#333;line-height:19px}
.hero-list li::before{content:"\25B6";color:var(--red);font-size:8px;margin-right:8px;vertical-align:1px}
.dots{position:absolute;left:330px;top:318px;display:flex;gap:5px}
.dots span{width:14px;height:3px;background:#bbb}
.dots span.on{background:var(--red)}
.services{position:absolute;top:418px;left:0;width:727px;height:92px;background:var(--dark);display:flex;padding:0 24px}
.service{flex:1;text-align:center;position:relative;padding-top:40px}
.service .icon{position:absolute;left:50%;top:-14px;margin-left:-22px;width:44px;height:44px;border-radius:50%;background:var(--red);border:3px solid var(--dark)}
.service h3{font-family:'Raleway',sans-serif;font-size:10px;font-weight:700;color:var(--red);letter-spacing:.4px}
.service p{font-size:7.5px;color:#bbb;margin:4px auto 0;width:120px;line-height:10px}
.service .more{font-size:7px;color:var(--white);font-weight:700;margin-top:4px;display:block}
.welcome{position:absolute;top:510px;left:0;width:727px;height:200px;background:var(--white)}
.welcome h2{position:absolute;left:30px;top:38px;font-family:'Raleway',sans-serif;font-size:22px;font-weight:700;color:var(--charcoal)}
.welcome h2 em{font-style:normal;color:var(--red)}
.welcome p{position:absolute;left:30px;top:74px;width:470px;font-size:8.5px;line-height:13px;color:var(--grey)}
.btn{display:inline-block;background:var(--red);color:var(--white);font-size:7.5px;font-weight:700;padding:6px 14px;letter-spacing:.4px}
.welcome .btn{position:absolute;left:30px;top:150px}
.welcome-photo{position:absolute;right:28px;top:22px;width:180px;height:160px;background:linear-gradient(135deg,#3a3a3a,#8a8a8a 55%,#d9d9d9)}
.area{position:absolute;top:710px;left:0;width:727px;height:290px;background:var(--light)}
.area h2{text-align:center;padding-top:30px;font-family:'Raleway',sans-serif;font-size:22px;font-weight:700;color:var(--charcoal)}
.area h2 em{font-style:normal;color:var(--red)}
.rule{width:90px;height:2px;background:var(--red);margin:6px auto 0}
.card{position:absolute;top:100px;width:320px;height:140px}
.card.one{left:30px}.card.two{left:377px}
.card-photo{position:absolute;left:0;top:0;width:150px;height:140px}
.card.one .card-photo{background:linear-gradient(180deg,#b8c9d9,#7b8a96 60%,#5a5f63)}
.card.two .card-photo{background:linear-gradient(180deg,#9bb27e,#6d7c60 55%,#4b4f55)}
.card-body{position:absolute;left:162px;top:4px;width:158px}
.card-body h3{font-family:'Raleway',sans-serif;font-size:13px;font-weight:700;line-height:16px;color:var(--charcoal)}
.card-body p{font-size:7.5px;line-height:11px;color:var(--grey);margin:8px 0 10px}
.footer{position:absolute;top:1000px;left:0;width:727px;height:170px;background:#1c1c1c;color:#ccc;display:flex;padding:30px 28px 0;gap:26px}
.footer h4{font-family:'Raleway',sans-serif;font-size:10px;font-weight:700;color:var(--white);margin-bottom:10px;letter-spacing:.4px}
.f-about{width:110px}
.f-about ul{list-style:none;font-size:8px;line-height:16px}
.f-about li::before{content:"\203A";color:var(--red);margin-right:6px}
.f-form{width:200px}
.f-form .row{display:flex;gap:6px;margin-bottom:6px}
.f-form .field{flex:1;height:18px;background:#2e2e2e;font-size:7px;color:#888;padding:4px 6px}
.f-form .area-field{height:34px;background:#2e2e2e;font-size:7px;color:#888;padding:4px 6px;margin-bottom:6px}
.f-contact{width:150px;font-size:8px;line-height:17px}
.f-contact svg{width:9px;height:9px;vertical-align:-1px;margin-right:6px;fill:var(--red)}
.f-follow .socials{display:flex;gap:6px}
.f-follow .socials span{width:22px;height:22px;border-radius:50%;background:var(--white)}
.bottom{position:absolute;top:1170px;left:0;width:727px;height:30px;background:var(--dark);display:flex;align-items:center;padding:0 28px;justify-content:space-between}
.bottom .brand-mini{display:flex;align-items:center;gap:6px;font-family:'Raleway',sans-serif;font-weight:800;font-size:10px;color:var(--white)}
.bottom .brand-mini i{width:14px;height:14px;background:var(--red);display:block}
.bottom small{font-size:7px;color:#999}
</style>
</head>
<body>
<header class="header">
  <div class="brand"><span class="brand-mark"></span><span class="brand-name">LARKMOOR BAILS Inc</span></div>
  <div class="topline">
    <svg width="10" height="10" viewBox="0 0 24 24"><path fill="#c4161c" d="M6.6 10.8a15 15 0 0 0 6.6 6.6l2.2-2.2c.3-.3.7-.4 1-.2 1.1.4 2.3.6 3.6.6.6 0 1 .4 1 1V20c0 .6-.4 1-1 1A17 17 0 0 1 3 4c0-.6.4-1 1-1h3.5c.6 0 1 .4 1 1 0 1.3.2 2.5.6 3.6.1.3 0 .7-.2 1z"/></svg>
    (555) 014 2200 <span class="dot"></span><span class="dot"></span><span class="dot"></span>
  </div>
  <nav class="nav">
    <a class="active">HOME</a><a>ABOUT US</a><a>WHAT WE OFFER</a><a>OUR SERVICE AREA</a><a>CONTACT US</a>
  </nav>
</header>

<section class="hero">
  <div class="hero-photo" role="img" aria-label="Steel ball and chain attached to an open handcuff"></div>
  <div class="hero-copy">
    <h1 class="hero-title">POWERFUL</h1>
    <p class="hero-sub">PROTECTION OF MY CLIENTS</p>
    <ul class="hero-list">
      <li>YOUR FREEDOM STARTS WITH LARKMOOR!</li>
      <li>LARKMOOR GETS YOU OUT. LARKMOOR GETS YOU HOME.</li>
      <li>WE GUARANTEE YOUR BAIL</li>
    </ul>
  </div>
  <div class="dots"><span class="on"></span><span></span><span></span><span></span></div>
</section>

<section class="services">
  <div class="service"><span class="icon"></span><h3>FELONY BAILS</h3><p>Fast release for serious charges, any hour.</p><span class="more">MORE ›</span></div>
  <div class="service"><span class="icon"></span><h3>DRUG CHARGE BAILS</h3><p>Discreet help posting bond for drug cases.</p><span class="more">MORE ›</span></div>
  <div class="service"><span class="icon"></span><h3>DUI BAILS</h3><p>Get home quickly after a DUI arrest.</p><span class="more">MORE ›</span></div>
  <div class="service"><span class="icon"></span><h3>TRAFFIC BAILS</h3><p>Simple bonds for traffic and license charges.</p><span class="more">MORE ›</span></div>
</section>

<section class="welcome">
  <h2>WELCOME TO <em>LARKMOOR BAILS Inc.</em></h2>
  <p>When someone you love is arrested, every hour matters. Our licensed agents work day and night to post bail quickly, explain each step clearly and keep your family informed from the first call until the release. We handle felony, drug, DUI and traffic cases across the region with care and respect.</p>
  <span class="btn">READ MORE</span>
  <div class="welcome-photo" role="img" aria-label="Businessman holding a chalkboard reading Know the rules"></div>
</section>

<section class="area">
  <h2>OUR SERVICE <em>AREA</em></h2>
  <div class="rule"></div>
  <div class="card one">
    <div class="card-photo" role="img" aria-label="City skyline of Western New York"></div>
    <div class="card-body">
      <h3>Serving all of Western New York</h3>
      <p>From Buffalo to Rochester, our agents reach every county courthouse and jail quickly, day or night.</p>
      <span class="btn">READ MORE ›</span>
    </div>
  </div>
  <div class="card two">
    <div class="card-photo" role="img" aria-label="Officer at a traffic stop beside a car"></div>
    <div class="card-body">
      <h3>At Larkmoor, our process is fast, Professional and Effective.</h3>
      <p>We answer every call, file paperwork fast and keep you updated until release.</p>
      <span class="btn">READ MORE ›</span>
    </div>
  </div>
</section>

<footer class="footer">
  <div class="f-about">
    <h4>ABOUT US</h4>
    <ul><li>Home</li><li>Services</li><li>What We Offer</li><li>Contact Us</li></ul>
  </div>
  <div class="f-form">
    <h4>CONTACT US</h4>
    <div class="row"><span class="field">Name</span><span class="field">Email</span></div>
    <div class="area-field">Message</div>
    <span class="btn">SUBMIT</span>
  </div>
  <div class="f-contact">
    <h4>HAVE QUESTIONS?</h4>
    <div><svg viewBox="0 0 24 24"><path d="M6.6 10.8a15 15 0 0 0 6.6 6.6l2.2-2.2c.3-.3.7-.4 1-.2 1.1.4 2.3.6 3.6.6.6 0 1 .4 1 1V20c0 .6-.4 1-1 1A17 17 0 0 1 3 4c0-.6.4-1 1-1h3.5c.6 0 1 .4 1 1 0 1.3.2 2.5.6 3.6.1.3 0 .7-.2 1z"/></svg>(555) 014 2200</div>
    <div><svg viewBox="0 0 24 24"><path d="M2 5h20v14H2zM2 5l10 8 10-8"/></svg>hello@larkmoorbails.example</div>
    <div><svg viewBox="0 0 24 24"><path d="M12 2a7 7 0 0 0-7 7c0 5 7 13 7 13s7-8 7-13a7 7 0 0 0-7-7zm0 9.5a2.5 2.5 0 1 1 0-5 2.5 2.5 0 0 1 0 5z"/></svg>214 Alder Row, Fenmoor, NY 14001</div>
  </div>
  <div class="f-follow">
    <h4>FOLLOW US</h4>
    <div class="socials"><span></span><span></span><span></span><span></span></div>
  </div>
</footer>

<div class="bottom">
  <div class="brand-mini"><i></i>LARKMOOR BAILS Inc</div>
  <small>Copy Right @ 2024 Company Name. All Rights Reserved.</small>
</div>
</body>
</html>
```